Rack Card Design Project

The New Feelings Marigny Cafe, Bar & Courtyard LoungeWe are totally new reimagined, rebranded, refocused cafe of which the name goes back nearly 50 years. www.lanterncafehall.example gives some more info.what we need is a simple postcard design with some great pictures on one side, and on the flip side simply just the name, address, website, etc. Our main font is SixCaps, and Engagement. Things to point out: new chef, new food, newly renovated, new atmosphere, new environment, new owners, same great historic charm, etc, etc. i have attached a bunch of files, and pics to choose from, as well as how we layout the "logo" on the menus. Our target audience is 30 - 55, locals and visitors who are looking for a unique, memorable dining and drinking experience. We are located just three blocks outside the Copper Ward, in the heart of the Perdido Landing area. Have fun, kick ass, wow us :-)

Target Market(s)

30 - 55 year olds

Industry/Entity Type

Cafe

Font styles to use
Serif
Sans Serif

Requirements
Must have
• must get the following points across:
• all new
• must be stylish and appealing in a classy upbeat way. (please watch the fonts used...nothing too crazy ;-)
Nice to have
• pictures of courtyard, dining room, exterior

```html
<!DOCTYPE html>
<html lang="en">
<head>
<meta charset="UTF-8">
<title>The All New Lantern – Rack Card</title>
<link rel="stylesheet" href="https://fonts.googleapis.com/css2?family=Antonio:wght@500;600&family=Engagement&family=Dancing+Script:wght@500;700&display=swap">
<style>
  :root {
    --backdrop: #e6e3de;
    --card-cream: #fbf9f0;
    --ink: #1d1a17;
    --brand-orange: #e8641e;
    --tagline-red: #a5141b;
    --band-red: #b3121a;
    --band-red-dark: #8e0c12;
    --swoosh-orange: #ef6a1c;
    --photo-border: #ffffff;
  }
  * { box-sizing: border-box; margin: 0; padding: 0; }
  html, body {
    width: 982px; height: 1200px; overflow: hidden;
    background: var(--backdrop);
  }
  .canvas {
    position: relative; width: 982px; height: 1200px;
  }
  .rack-card {
    position: absolute; left: 237px; top: 30px;
    width: 508px; height: 1140px;
    background: var(--card-cream);
    overflow: hidden;
    box-shadow: 0 6px 22px rgba(0,0,0,.25);
  }
  .eyebrow {
    position: absolute; top: 42px; left: 0; right: 0;
    text-align: center;
    font-family: "Engagement", "Dancing Script", cursive;
    font-size: 44px; color: var(--ink); line-height: 1;
  }
  .brand-name {
    position: absolute; top: 88px; left: 0; right: 0;
    text-align: center;
    font-family: "Antonio", "Oswald", sans-serif;
    font-weight: 600; font-size: 132px; letter-spacing: 2px;
    color: var(--brand-orange); line-height: 1;
    text-transform: uppercase;
  }
  .venue-line {
    position: absolute; top: 262px; left: 0; right: 0;
    text-align: center;
    font-family: "Engagement", "Dancing Script", cursive;
    font-size: 31px; color: var(--ink); line-height: 1;
  }
  .collage-haze {
    position: absolute; left: 20px; top: 330px; width: 468px; height: 500px;
    background: linear-gradient(160deg, rgba(190,150,160,.18), rgba(160,170,150,.16) 50%, rgba(170,160,150,.2));
    filter: blur(6px);
  }
  .photo {
    position: absolute;
    background: var(--photo-border);
    padding: 6px;
    box-shadow: 2px 4px 10px rgba(0,0,0,.35);
  }
  .photo-fill { width: 100%; height: 100%; }
  .photo--courtyard-night { left: 148px; top: 345px; width: 318px; height: 165px; transform: rotate(-5deg); }
  .photo--courtyard-night .photo-fill { background: linear-gradient(120deg, #4a4240 0%, #6b4c6e 45%, #9a3fb8 70%, #5a2f7a 100%); }
  .photo--exterior { left: 62px; top: 500px; width: 182px; height: 145px; transform: rotate(4deg); }
  .photo--exterior .photo-fill { background: linear-gradient(180deg, #2a2622 0%, #6e5a3e 45%, #d8c8a4 70%, #3a2e22 100%); }
  .photo--garden-lounge { left: 300px; top: 548px; width: 160px; height: 112px; transform: rotate(3deg); }
  .photo--garden-lounge .photo-fill { background: linear-gradient(140deg, #3f5a3a 0%, #c04a5a 50%, #7a8a80 100%); }
  .photo--dining-room { left: 78px; top: 668px; width: 220px; height: 150px; transform: rotate(-6deg); }
  .photo--dining-room .photo-fill { background: linear-gradient(160deg, #3a2a22 0%, #8a7060 40%, #d6d0c8 75%, #5a4a40 100%); }
  .photo--entrance-flags { left: 296px; top: 692px; width: 168px; height: 128px; transform: rotate(-4deg); }
  .photo--entrance-flags .photo-fill { background: linear-gradient(150deg, #2a2030 0%, #8a2a34 45%, #c8503a 70%, #3a2a30 100%); }
  .tagline {
    position: absolute; top: 850px; left: 20px; right: 20px;
    text-align: center;
    font-family: "Engagement", "Dancing Script", cursive;
    font-size: 35px; line-height: 1.15; color: var(--tagline-red);
  }
  .footer-band {
    position: absolute; left: 0; bottom: 0; width: 508px; height: 160px;
  }
  .website {
    position: absolute; left: 0; right: 0; bottom: 34px;
    display: flex; justify-content: center; align-items: center; gap: 12px;
    font-family: "Engagement", "Dancing Script", cursive;
    font-size: 28px; color: #ffffff;
  }
  .website svg { width: 20px; height: 20px; }
</style>
</head>
<body>
<div class="canvas">
  <article class="rack-card">
    <p class="eyebrow">The All New</p>
    <h1 class="brand-name">Lantern</h1>
    <p class="venue-line">Bayside Cafe, Bar &amp; Garden Parlor</p>

    <div class="collage-haze" role="img" aria-label="Soft blurred photo of the cafe interior behind the collage"></div>
    <div class="photo photo--courtyard-night"><div class="photo-fill" role="img" aria-label="Courtyard lounge at night with sofas and purple lighting"></div></div>
    <div class="photo photo--exterior"><div class="photo-fill" role="img" aria-label="Building exterior at night with palm trees and string lights"></div></div>
    <div class="photo photo--garden-lounge"><div class="photo-fill" role="img" aria-label="Garden lounge seating with red cushions among plants"></div></div>
    <div class="photo photo--dining-room"><div class="photo-fill" role="img" aria-label="Dining room with chandelier, set tables and framed pictures"></div></div>
    <div class="photo photo--entrance-flags"><div class="photo-fill" role="img" aria-label="Entrance at night with flags and a lit sign"></div></div>

    <p class="tagline">New Chef, New Food, New Vibe,<br>New Look,<br>Its a Whole New Feel!</p>

    <svg class="footer-band" viewBox="0 0 508 160" preserveAspectRatio="none" aria-hidden="true">
      <defs>
        <linearGradient id="bandShade" x1="0" y1="0" x2="0" y2="1">
          <stop offset="0" stop-color="var(--band-red)"/>
          <stop offset="1" stop-color="var(--band-red-dark)"/>
        </linearGradient>
      </defs>
      <path d="M0,56 Q250,52 508,0 L508,26 Q250,68 0,62 Z" fill="var(--swoosh-orange)"/>
      <path d="M0,68 Q260,72 508,34 L508,160 L0,160 Z" fill="url(#bandShade)"/>
    </svg>
    <p class="website">
      <svg viewBox="0 0 20 20" aria-hidden="true" fill="none" stroke="#fff" stroke-width="1.6">
        <circle cx="10" cy="10" r="8"/>
        <ellipse cx="10" cy="10" rx="3.6" ry="8"/>
        <line x1="2" y1="10" x2="18" y2="10"/>
      </svg>
      www.lanterncafehall.example
    </p>
  </article>
</div>
</body>
</html>
```